RIVO graphic design elements

RIVO is a group of schools who have adopted positive psychology as the framework for their wellbeing programs.

Designs should be simple and formal (rather than ultra modern/trendy)

I require quotes for the following:
Letterhead
Business Card
Powerpoint slides
Pull up banner (approx 2m high)
Colour pallette development

I have uploaded a copy of our logo

```html
<!DOCTYPE html>
<html lang="en">
<head>
<meta charset="utf-8">
<title>RIVO – Sales of The Month</title>
<link rel="stylesheet" href="https://fonts.googleapis.com/css2?family=Open+Sans:wght@400;600;700;800&display=swap">
<style>
  :root {
    --page-bg: #ecebe8;
    --slide-bg: #ffffff;
    --brand-orange: #f68b1f;
    --brand-red: #e42b36;
    --brand-blue: #1f6fb5;
    --bar-blue: #94cddc;
    --accent-teal: #2f7f98;
    --ink: #111111;
    --muted: #555555;
    --rule: #c9c9c9;
    --grid: #c5d3d8;
  }
  * { margin: 0; padding: 0; box-sizing: border-box; }
  html, body {
    width: 1200px; height: 1000px; overflow: hidden;
    background: var(--page-bg);
    font-family: "Open Sans", Arial, sans-serif;
  }
  .slide {
    position: absolute; left: 84px; top: 136px;
    width: 1033px; height: 728px;
    background: var(--slide-bg);
    box-shadow: 0 4px 18px rgba(0,0,0,.18);
    overflow: hidden;
  }
  .brand {
    position: absolute; left: 34px; top: 38px;
    display: flex; align-items: center; gap: 14px;
  }
  .brand-mark { width: 48px; height: 48px; background: var(--brand-red); }
  .brand-name {
    font-weight: 800; font-size: 52px; line-height: 1;
    color: var(--brand-blue); letter-spacing: 1px;
  }
  .header-band {
    position: absolute; left: 287px; right: 0; top: 37px; height: 62px;
    background: var(--brand-orange);
    display: flex; align-items: center; padding-left: 24px;
  }
  .header-title {
    color: #fff; font-weight: 700; font-size: 17px; letter-spacing: 1.2px;
  }
  .footer-band {
    position: absolute; left: 0; right: 0; bottom: 0; height: 21px;
    background: var(--brand-orange);
  }
  .chart-card {
    position: absolute; left: 156px; top: 202px;
    width: 742px; height: 380px;
    border: 2px solid var(--rule);
  }
  .chart-card svg { position: absolute; left: -2px; top: -2px; }
  .chart-title { font-weight: 700; font-size: 19px; fill: var(--ink); }
  .bar { fill: var(--bar-blue); }
  .bar-grid { stroke: #fff; stroke-width: 3; }
  .value-label { font-size: 12.5px; fill: var(--ink); text-anchor: middle; }
  .tick-label { font-size: 11px; fill: var(--muted); text-anchor: end; }
  .axis-label { font-size: 11px; fill: var(--muted); text-anchor: middle; }
  .axis-line { stroke: #888; stroke-width: 1; }
  .callout-line { stroke: var(--accent-teal); stroke-width: 2; fill: none; }
  .callout-text { font-weight: 600; font-size: 17px; fill: var(--accent-teal); text-anchor: middle; }
  .ref-line { stroke: var(--grid); stroke-width: 1.2; }
  .ref-text { font-size: 12.5px; fill: var(--accent-teal); text-anchor: middle; }
  .big-number { font-weight: 800; font-size: 30px; fill: var(--ink); text-anchor: middle; }
  .base-label { font-size: 16px; fill: var(--accent-teal); }
</style>
</head>
<body>
<main class="slide">
  <div class="brand">
    <span class="brand-mark"></span>
    <span class="brand-name">RIVO</span>
  </div>
  <header class="header-band"><h1 class="header-title">Sales of The Month</h1></header>

  <section class="chart-card">
    <svg width="742" height="380" viewBox="0 0 742 380" role="img" aria-label="Bar chart of premiums by age range">
      <text class="chart-title" x="28" y="31">Premiums for those age 60+ are 4.4 times base rate ( age 0-18)</text>

      <!-- reference line -->
      <line class="ref-line" x1="66" y1="171" x2="190" y2="171"/>
      <line class="ref-line" x1="284" y1="171" x2="660" y2="171"/>
      <text class="ref-text" x="236" y="175">3x base rate</text>

      <!-- axis -->
      <line class="axis-line" x1="60" y1="73" x2="60" y2="326"/>
      <line class="axis-line" x1="60" y1="326" x2="716" y2="326"/>
      <g>
        <text class="tick-label" x="52" y="330">0</text>
        <text class="tick-label" x="52" y="279">70</text>
        <text class="tick-label" x="52" y="228">140</text>
        <text class="tick-label" x="52" y="178">210</text>
        <text class="tick-label" x="52" y="127">280</text>
        <text class="tick-label" x="52" y="77">350</text>
      </g>
      <text class="axis-label" transform="translate(16 200) rotate(-90)">Premiums ($USD)</text>

      <!-- bars -->
      <g>
        <rect class="bar" x="72"  y="274.7" width="48" height="51.3"/>
        <rect class="bar" x="138" y="255.9" width="48" height="70.1"/>
        <rect class="bar" x="204" y="244.3" width="48" height="81.7"/>
        <rect class="bar" x="270" y="232.0" width="48" height="94.0"/>
        <rect class="bar" x="335" y="219.0" width="48" height="107.0"/>
        <rect class="bar" x="401" y="203.1" width="48" height="122.9"/>
        <rect class="bar" x="467" y="193.7" width="48" height="132.3"/>
        <rect class="bar" x="532" y="176.4" width="48" height="149.6"/>
        <rect class="bar" x="598" y="146.7" width="48" height="179.3"/>
        <rect class="bar" x="663" y="99.0"  width="48" height="227.0"/>
      </g>
      <g>
        <line class="bar-grid" x1="66" y1="275.4" x2="716" y2="275.4"/>
        <line class="bar-grid" x1="335" y1="224.8" x2="716" y2="224.8"/>
        <line class="bar-grid" x1="598" y1="174.2" x2="716" y2="174.2"/>
        <line class="bar-grid" x1="663" y1="123.6" x2="716" y2="123.6"/>
      </g>

      <!-- values -->
      <g>
        <text class="value-label" x="162" y="247">97</text>
        <text class="value-label" x="228" y="236">113</text>
        <text class="value-label" x="294" y="224">130</text>
        <text class="value-label" x="359" y="211">148</text>
        <text class="value-label" x="425" y="195">170</text>
        <text class="value-label" x="491" y="186">183</text>
        <text class="value-label" x="556" y="168">207</text>
        <text class="value-label" x="622" y="139">248</text>
      </g>

      <!-- x labels -->
      <g>
        <text class="axis-label" x="96"  y="346">0-18</text>
        <text class="axis-label" x="162" y="346">19-24</text>
        <text class="axis-label" x="228" y="346">25-29</text>
        <text class="axis-label" x="294" y="346">30-34</text>
        <text class="axis-label" x="359" y="346">35-39</text>
        <text class="axis-label" x="425" y="346">40-44</text>
        <text class="axis-label" x="491" y="346">45-49</text>
        <text class="axis-label" x="556" y="346">50-54</text>
        <text class="axis-label" x="622" y="346">55-59</text>
        <text class="axis-label" x="687" y="346">60-64</text>
      </g>
      <text class="axis-label" x="387" y="366">Age Range</text>
      <text class="base-label" x="61" y="371">base rate</text>

      <!-- callout -->
      <path class="callout-line" d="M91 234 V74 H228"/>
      <line class="callout-line" x1="394" y1="74" x2="660" y2="74"/>
      <text class="callout-text" x="311" y="81">4.4x base rate</text>
      <text class="big-number" x="94" y="268">71</text>
      <text class="big-number" x="686" y="87">314</text>
    </svg>
  </section>

  <div class="footer-band"></div>
</main>
</body>
</html>
```